Brochure required for international Sports event

We need an 8 page brochure designed for an international sports event to be hosted in Japan. We are a Travel Company providing packages for participants looking to travel to the event.
The brochure will feature information on the event as well as services our company can provide.
The Brochure is to be an 8 page A4 document in portrait layout.
The brochure needs to be provided both as a print ready document and digital brochure for emailing.
Brochure structure, copy, logo and imagery has been provided
As well as a example brochure design that we like for inspiration.
Link to icons - https://www.filorabox.com/sh/qk3ramvi8ptyzel/BBBqwLpRt7VmK3H9nX2cT8gRb?dl=0
Target Market(s)
Masters/Veterans Sports Participants
Industry/Entity Type
Travel
Colors
Designer to choose colors to be used in the design.
Look and feel

```html
<!DOCTYPE html>
<html lang="en">
<head>
<meta charset="utf-8">
<title>Global Veterans Games 2021 – Travel Brochure</title>
<link href="https://fonts.googleapis.com/css2?family=Oswald:wght@400;600;700&family=Open+Sans:wght@400;600;700&display=swap" rel="stylesheet">
<style>
:root{
  --stage:#e4e4e4;
  --ink:#2b2b2d;
  --ink-soft:#3a3a3d;
  --red:#d8262c;
  --paper:#f3f3f3;
  --muted:#b9b9bc;
  --line:#55555a;
}
*{box-sizing:border-box;margin:0;padding:0}
html,body{width:1200px;height:3972px;overflow:hidden;background:var(--stage)}
body{font-family:"Open Sans",Arial,sans-serif;color:var(--ink)}
.band{height:794.4px;display:flex;align-items:center;justify-content:center;border-bottom:1px solid #d2d2d2}
.page{position:relative;overflow:hidden;box-shadow:0 2px 10px rgba(0,0,0,.18)}
.single{width:400px;height:566px}
.spread{display:flex;box-shadow:0 4px 18px rgba(0,0,0,.2)}
.spread .page{width:380px;height:537px;box-shadow:none}
.dark{background:var(--ink);color:#e8e8e8}
.light{background:var(--paper)}
.head{font-family:"Oswald",Arial,sans-serif;font-weight:700;text-transform:uppercase;line-height:1.1}
.red{color:var(--red)}
.small{font-size:6.5px;line-height:1.55}

/* event name set as plain text with one square */
.wordmark{display:flex;align-items:center;gap:8px;font-family:"Oswald",Arial,sans-serif;font-weight:600;text-transform:uppercase;white-space:nowrap}
.wordmark .sq{width:12px;height:12px;background:var(--red);flex:none}

/* cover */
.cover-top{position:absolute;inset:0 0 160px 0;background:var(--ink)}
.cover-rule{position:absolute;left:40px;right:40px;top:70px;height:4px;background:var(--red)}
.cover-name{position:absolute;left:0;right:0;top:150px;justify-content:center;color:#fff;font-size:28px}
.cover-sub{position:absolute;left:0;right:0;top:200px;text-align:center;font-family:"Oswald",sans-serif;font-size:13px;letter-spacing:3px;color:var(--muted)}
.icon-row{position:absolute;left:40px;right:40px;top:318px;display:flex;justify-content:space-between}
.icon-row i{width:18px;height:18px;border-radius:50%;border:2px solid #fff;display:block}
.cover-foot{position:absolute;left:0;right:0;bottom:0;height:160px;background:var(--paper);text-align:center;padding-top:40px}
.cover-foot .place{font-size:34px;color:var(--red)}
.cover-foot .date{font-family:"Oswald",sans-serif;font-size:14px;color:var(--ink);margin-top:6px;letter-spacing:1px}

/* welcome */
.welcome{padding:40px 34px}
.welcome h2{font-size:28px;color:var(--ink);margin-top:40px}
.welcome p{margin-top:10px;color:#555}
.welcome .sign{position:absolute;bottom:34px;left:34px;font-size:20px}
.corner-mark{position:absolute;top:30px;right:30px;font-size:11px;color:var(--ink)}
.sports{padding:34px 30px}
.sports h3{font-size:13px;color:#fff;border-bottom:1px solid var(--line);padding-bottom:8px;margin-bottom:14px}
.sport-list{display:grid;grid-template-columns:1fr 1fr;gap:9px 16px;list-style:none}
.sport-list li{display:flex;align-items:center;gap:8px;font-size:8px;color:#ddd}
.sport-list li::before{content:"";width:16px;height:16px;border-radius:50%;background:#fff;flex:none}

/* map spread */
.map{position:absolute;left:20px;right:20px;top:30px;height:300px;background:linear-gradient(135deg,#3fa9e0,#8fd16a 35%,#f4c23a 60%,#e9573f 80%,#b05bc9)}
.map-caption{position:absolute;left:30px;right:30px;top:360px}
.map-caption h2{font-size:26px}
.map-caption p{margin-top:8px;color:#555}
.info{padding:34px 30px}
.info h3{font-size:13px;color:var(--red);margin:16px 0 6px}
.info h3:first-child{margin-top:0}
.info p{color:#cfcfcf}

/* hotels and partners */
.photo{position:absolute;background:linear-gradient(135deg,#6b5a44,#a88a62 60%,#3e3a36)}
.p1{left:24px;top:60px;width:200px;height:110px}
.p2{left:24px;top:182px;width:150px;height:110px}
.p3{left:186px;top:182px;width:170px;height:110px}
.partners-title{position:absolute;left:24px;top:30px;font-size:12px;color:#fff}
.partners{position:absolute;left:0;right:0;bottom:0;height:200px;background:var(--paper);padding:22px 24px}
.partners h3{font-size:22px;color:var(--red)}
.badges{display:flex;flex-wrap:wrap;gap:14px 20px;margin-top:18px}
.badge{display:flex;align-items:center;gap:6px;font-family:"Oswald",sans-serif;font-size:13px;font-weight:600;color:var(--ink)}
.badge i{width:28px;height:18px;background:var(--muted);display:block}
.schedule{padding:30px 22px}
.schedule h3{font-size:12px;color:#fff;margin-bottom:10px}
table{width:100%;border-collapse:collapse;background:#fff;color:#333;font-size:6.5px}
th{background:var(--red);color:#fff;text-align:left;padding:4px;font-weight:600}
td{padding:4px;border-bottom:1px solid #ddd}
tr:nth-child(even) td{background:#f1f1f1}

/* back cover */
.back-rule{position:absolute;left:40px;right:40px;top:70px;height:4px;background:var(--red)}
.back-name{position:absolute;left:0;right:0;top:150px;justify-content:center;color:#fff;font-size:24px}
.back-text{position:absolute;left:0;right:0;top:300px;text-align:center}
.back-text .head{font-size:20px;color:#fff}
.back-text .head.red{font-size:26px;color:var(--red)}
.contact{margin-top:22px;font-size:8px;color:#cfcfcf;line-height:1.8}
.socials{position:absolute;bottom:36px;left:50%;transform:translateX(-50%);display:flex;gap:8px}
.socials i{width:16px;height:16px;background:var(--red);display:block}
</style>
</head>
<body>

<section class="band">
  <div class="page single">
    <div class="cover-top">
      <div class="cover-rule"></div>
      <div class="wordmark cover-name"><span class="sq"></span><span>Global Veterans Games</span></div>
      <div class="cover-sub">2021 TRAVEL PACKAGES</div>
      <div class="icon-row"><i></i><i></i><i></i><i></i><i></i><i></i><i></i><i></i><i></i><i></i><i></i><i></i></div>
    </div>
    <div class="cover-foot">
      <div class="head place">Kansai, Japan</div>
      <div class="date">14 – 30 MAY 2021</div>
    </div>
  </div>
</section>

<section class="band">
  <div class="spread">
    <div class="page light welcome">
      <div class="corner-mark wordmark"><span class="sq"></span><span>Global Veterans Games</span></div>
      <h2 class="head"><span class="red">Welcome</span> to the<br>Global Veterans<br>Games<br>in <span class="red">Kansai, Japan</span></h2>
      <p class="small">Join thousands of masters athletes from around the world for two weeks of sport, friendship and culture across the Kansai region. Our team takes care of flights, hotels and transfers so you can focus on your event.</p>
      <p class="small">Every package includes accommodation close to your venue, airport transfers, local support staff and a welcome pack with maps, timetables and travel tips for your stay in Japan.</p>
      <p class="small">Compete, explore historic cities, taste regional food and meet fellow competitors at social evenings held throughout the Games. Spaces are limited, so book early to secure your place.</p>
      <p class="small">Travel with friends, family or your club team. We offer flexible dates, extension tours and group rates for parties of ten or more travellers.</p>
      <div class="sign head">Let the <span class="red">Games</span> begin!</div>
    </div>
    <div class="page dark sports">
      <h3 class="head">Sports &amp; Disciplines</h3>
      <ul class="sport-list">
        <li>Archery</li><li>Athletics</li><li>Badminton</li><li>Baseball</li><li>Basketball</li><li>Beach Volleyball</li><li>Bowling</li><li>Canoe</li><li>Cycling</li><li>Football</li><li>Golf</li><li>Handball</li><li>Hockey</li><li>Judo</li><li>Karate</li><li>Orienteering</li><li>Rowing</li><li>Rugby</li><li>Sailing</li><li>Shooting</li><li>Softball</li><li>Squash</li><li>Swimming</li><li>Table Tennis</li><li>Tennis</li><li>Triathlon</li><li>Volleyball</li><li>Weightlifting</li>
      </ul>
    </div>
  </div>
</section>

<section class="band">
  <div class="spread">
    <div class="page light">
      <div class="map" role="img" aria-label="Colour-coded venue map of the Kansai region showing sports locations"></div>
      <div class="map-caption">
        <h2 class="head">Official <span class="red">Venue Map</span></h2>
        <p class="small">Getting around the region is simple with fast trains linking every venue city.</p>
      </div>
    </div>
    <div class="page dark info">
      <h3 class="head">Getting There</h3>
      <p class="small">Fly direct into Kansai International Airport, with private transfers to your hotel on arrival and departure.</p>
      <h3 class="head">Where to Stay</h3>
      <p class="small">Choose from city hotels, traditional inns or apartments, all selected for easy access to venues.</p>
      <h3 class="head">Getting Around</h3>
      <p class="small">Rail passes are included in every package, covering trains between Osaka, Kyoto, Kobe and Nara.</p>
      <h3 class="head">Explore Kansai</h3>
      <p class="small">Add guided day tours to temples, gardens, castles and food markets before or after your event.</p>
      <h3 class="head">On the Ground</h3>
      <p class="small">Our local team is available every day of the Games to help with tickets, transport and bookings.</p>
    </div>
  </div>
</section>

<section class="band">
  <div class="spread">
    <div class="page dark">
      <div class="partners-title head">Your Hotel Options</div>
      <div class="photo p1" role="img" aria-label="Hotel lobby photograph"></div>
      <div class="photo p2" role="img" aria-label="Hotel room photograph"></div>
      <div class="photo p3" role="img" aria-label="Hotel restaurant photograph"></div>
      <div class="partners">
        <h3 class="head">Airline Partners</h3>
        <div class="badges">
          <span class="badge"><i></i>Skyline Air</span>
          <span class="badge"><i></i>Harbor Wings</span>
          <span class="badge"><i></i>Sakura Jet</span>
          <span class="badge"><i></i>Orbit Sport Travel</span>
        </div>
      </div>
    </div>
    <div class="page dark schedule">
      <h3 class="head">Competition Schedule</h3>
      <table>
        <thead><tr><th>Sport</th><th>Venue</th><th>City</th><th>Dates</th></tr></thead>
        <tbody>
          <tr><td>Athletics</td><td>Main Stadium</td><td>Osaka</td><td>15–20 May</td></tr>
          <tr><td>Swimming</td><td>Aquatic Centre</td><td>Osaka</td><td>16–21 May</td></tr>
          <tr><td>Cycling</td><td>Road Circuit</td><td>Shiga</td><td>18–22 May</td></tr>
          <tr><td>Football</td><td>Park Fields</td><td>Kobe</td><td>15–25 May</td></tr>
          <tr><td>Golf</td><td>Hill Course</td><td>Hyogo</td><td>19–23 May</td></tr>
          <tr><td>Rowing</td><td>Lake Course</td><td>Shiga</td><td>20–24 May</td></tr>
          <tr><td>Tennis</td><td>Court Centre</td><td>Kyoto</td><td>16–22 May</td></tr>
          <tr><td>Judo</td><td>Martial Hall</td><td>Nara</td><td>21–23 May</td></tr>
          <tr><td>Basketball</td><td>City Arena</td><td>Osaka</td><td>17–26 May</td></tr>
          <tr><td>Triathlon</td><td>Bay Course</td><td>Wakayama</td><td>24–25 May</td></tr>
          <tr><td>Softball</td><td>Ball Park</td><td>Kyoto</td><td>18–24 May</td></tr>
          <tr><td>Sailing</td><td>Marina</td><td>Wakayama</td><td>22–27 May</td></tr>
          <tr><td>Squash</td><td>Sports Hall</td><td>Kobe</td><td>23–26 May</td></tr>
          <tr><td>Hockey</td><td>Turf Stadium</td><td>Osaka</td><td>19–28 May</td></tr>
          <tr><td>Volleyball</td><td>Dome Arena</td><td>Kyoto</td><td>20–29 May</td></tr>
          <tr><td>Archery</td><td>Range Park</td><td>Nara</td><td>25–28 May</td></tr>
        </tbody>
      </table>
    </div>
  </div>
</section>

<section class="band">
  <div class="page single dark">
    <div class="back-rule"></div>
    <div class="wordmark back-name"><span class="sq"></span><span>Global Veterans Games</span></div>
    <div class="back-text">
      <div class="head">The 2021 Global Veterans Games</div>
      <div class="head">See you soon in</div>
      <div class="head red">Kansai, Japan</div>
      <div class="contact">www.orbitsporttravel.example<br>bookings@orbitsporttravel.example<br>+00 1234 567 890</div>
    </div>
    <div class="socials"><i></i><i></i><i></i></div>
  </div>
</section>

</body>
</html>
```